TaleBeacons business card for creator of IP TOY (fun) (children) designs

This business card will be the introduction of me as the creator of new designs to the toy industry and beyond. These designs are kept secret until being revealed one on one to each company. My design is patent pending protected IP. I am looking for business appropriate with a tinge of fun. Please no black backgounds as this is the toy industry. Be creative with the logo and colors please. Just imagine.

Target Market(s)

TOY Industry Executives - Inventor Relations - Manufacturers this is my first introduction card.

Industry/Entity Type

Toy Industry - I have included our Brand colors which can be seen on the cover of The Tiny Blue Goat book so uses for any of these others colors would be intersting.

Contact Information for Business Card

LOGO Delia Vantreck Founder Creator 214 555 0182 2817 E Mallow Ridge Anna, TX 75288 www.talebeacons.example deliavantreck@mailhollow.example Patent Pending IP

Font styles to use
Other font styles liked:
• The font used in the logo is Swiss721BT bold I need to see other fonts to be able to decide but need a clean look

Requirements
Must have
• A bit of an artistic flair although the logo is very simple. I am in the toy industry so would like something that sparks the look of being a creator?
Nice to have
• Please try a background other than stark white. Would like to see a play using brand colors?I like the logos which look like they are lifted off the page. Then under the logo the words (not lifted?) Any Action Any Character Any Teaching
Should not have
• No Black Backgrounds please! should look as clean as possible - I am not opposed to changing to a double sided card if that is more effectual.

```html
<!DOCTYPE html>
<html lang="en">
<head>
<meta charset="utf-8">
<title>TaleBeacons Business Card</title>
<link rel="stylesheet" href="https://fonts.googleapis.com/css2?family=Lato:wght@400;700;900&display=swap">
<style>
  :root {
    --brand-red: #d6001c;
    --band-red: #c10f26;
    --paper: #ffffff;
    --ink: #1a1a1a;
    --stage: #d9d9dc;
  }
  * { margin: 0; padding: 0; box-sizing: border-box; }
  html, body {
    width: 1200px;
    height: 694px;
    overflow: hidden;
    background: var(--stage);
    font-family: "Lato", Arial, sans-serif;
  }
  .sheet {
    position: relative;
    width: 1200px;
    height: 694px;
    display: flex;
    align-items: center;
    justify-content: center;
    gap: 40px;
  }
  .card {
    position: relative;
    width: 540px;
    height: 309px;
    border-radius: 24px;
    overflow: hidden;
  }
  .card-front {
    background: var(--brand-red);
    display: flex;
    align-items: center;
    justify-content: center;
  }
  .front-wordmark {
    color: var(--paper);
    font-weight: 900;
    font-size: 68px;
    letter-spacing: -1px;
  }
  .card-back { background: var(--paper); color: var(--ink); }
  .back-wordmark {
    position: absolute;
    top: 52px;
    right: 46px;
    color: var(--brand-red);
    font-weight: 900;
    font-size: 40px;
    letter-spacing: -0.5px;
  }
  .holder {
    position: absolute;
    left: 60px;
    top: 158px;
  }
  .holder-name {
    color: var(--brand-red);
    font-weight: 700;
    font-size: 22px;
    line-height: 1.1;
  }
  .holder-role {
    font-size: 15px;
    margin-top: 2px;
    margin-left: 18px;
  }
  .divider {
    position: absolute;
    left: 58px;
    right: 36px;
    top: 215px;
    height: 1px;
    background: var(--ink);
  }
  .contact-list {
    position: absolute;
    left: 64px;
    top: 224px;
    list-style: none;
    font-size: 14px;
    line-height: 20px;
  }
  .contact-list li { display: flex; align-items: center; gap: 8px; }
  .contact-list svg { width: 13px; height: 13px; flex: none; }
  .address {
    position: absolute;
    right: 40px;
    top: 222px;
    text-align: right;
    font-size: 13px;
    line-height: 18px;
  }
  .bottom-band {
    position: absolute;
    left: 0;
    bottom: 0;
    width: 540px;
    height: 48px;
  }
  .website {
    position: absolute;
    right: 30px;
    bottom: 8px;
    color: var(--paper);
    font-size: 12.5px;
  }
</style>
</head>
<body>
<main class="sheet">
  <section class="card card-front" aria-label="Card front">
    <span class="front-wordmark">TaleBeacons</span>
  </section>

  <section class="card card-back" aria-label="Card back">
    <span class="back-wordmark">TaleBeacons</span>

    <div class="holder">
      <p class="holder-name">Delia Vantreck</p>
      <p class="holder-role">Founder Creator</p>
    </div>

    <div class="divider"></div>

    <ul class="contact-list">
      <li>
        <svg viewBox="0 0 16 16" aria-hidden="true"><path fill="var(--brand-red)" d="M3.6 1.5l2.3 2.6-1.2 1.8c.9 2 2.4 3.5 4.4 4.4l1.8-1.2 2.6 2.3-1.5 2.4C6.6 13.6 2.4 9.4 1.2 4.1z"/></svg>
        214 555 0182
      </li>
      <li>
        <svg viewBox="0 0 16 16" aria-hidden="true"><rect x="1" y="3" width="14" height="10" fill="var(--brand-red)"/><path d="M1 3l7 6 7-6" fill="none" stroke="#fff" stroke-width="1.3"/></svg>
        deliavantreck@mailhollow.example
      </li>
    </ul>

    <p class="address">2817 E Mallow Ridge<br>Anna, TX 75288</p>

    <svg class="bottom-band" viewBox="0 0 540 48" preserveAspectRatio="none" aria-hidden="true">
      <path d="M0 40 L330 40 L345 30 L350 14 L540 14 L540 48 L0 48 Z" fill="var(--band-red)"/>
      <path d="M0 34 L330 34 L343 25" fill="none" stroke="var(--band-red)" stroke-width="3"/>
    </svg>
    <span class="website">www.talebeacons.example</span>
  </section>
</main>
</body>
</html>
```